Business Card for TVK, logo files already created

Please, can you assist with creating a Business card the TVK graphics which are already listed on www.brinmoretech.example
The business card should be modern and upmarket, textured designs are welcome. Please feel free to express yourself and be very bold with your design.

Target Market(s)

Cyber Security

Industry/Entity Type

Information Technology

Contact Information for Business Card

Company Name
Name
Title
Mobile
Fax or Tel
email
url

Font styles to use
Serif
Sans Serif

Colors
3277b5
85acd3
ffffff

```html
<!DOCTYPE html>
<html lang="en">
<head>
<meta charset="utf-8">
<title>TVK Business Card</title>
<link rel="stylesheet" href="https://fonts.googleapis.com/css2?family=Archivo:wght@400;700;900&family=Arimo:wght@400;700&display=swap">
<style>
  :root {
    --stage: #262626;
    --card: #0d0d0e;
    --card-edge: #1a1a1b;
    --silver: #b9b9bb;
    --silver-dim: #8a8a8c;
    --blue: #3277b5;
    --blue-light: #85acd3;
    --white: #ffffff;
    --text-grey: #c9c9cb;
    --rule: #5a5a5c;
  }
  * { margin: 0; padding: 0; box-sizing: border-box; }
  html, body { width: 1200px; height: 1200px; overflow: hidden; }
  body {
    background: var(--stage);
    display: flex;
    flex-direction: column;
    align-items: center;
    justify-content: center;
    gap: 36px;
    font-family: "Arimo", Arial, sans-serif;
  }
  .card {
    width: 880px;
    height: 500px;
    background: var(--card);
    border: 1px solid var(--card-edge);
    position: relative;
    overflow: hidden;
  }
  /* Back side */
  .card-back {
    display: flex;
    flex-direction: column;
    align-items: center;
    justify-content: center;
    background: linear-gradient(160deg, #161617 0%, #0a0a0b 70%);
  }
  .brand-name {
    font-family: "Archivo", Arial, sans-serif;
    font-weight: 900;
    letter-spacing: 4px;
    line-height: 1;
  }
  .card-back .brand-name { font-size: 130px; color: var(--silver); }
  .tagline {
    font-family: "Archivo", Arial, sans-serif;
    font-weight: 400;
    letter-spacing: 4px;
    text-transform: uppercase;
    white-space: nowrap;
  }
  .card-back .tagline { font-size: 19px; color: var(--silver-dim); margin-top: 22px; }
  .card-back .back-url {
    position: absolute;
    bottom: 70px;
    left: 0; right: 0;
    text-align: center;
    font-family: "Archivo", Arial, sans-serif;
    font-weight: 700;
    font-size: 18px;
    letter-spacing: 3px;
    color: var(--silver-dim);
  }
  /* Front side */
  .card-front { display: flex; align-items: center; padding-left: 20px; }
  .texture {
    position: absolute;
    inset: 0;
    background: radial-gradient(ellipse at 40% 30%, #1c1c1e 0%, #101011 55%, #0b0b0c 100%);
  }
  .front-logo {
    position: relative;
    width: 400px;
    display: flex;
    flex-direction: column;
    align-items: center;
  }
  .front-logo .brand-name { font-size: 112px; color: var(--blue); }
  .front-logo .tagline { font-size: 15px; color: var(--blue); margin-top: 20px; letter-spacing: 3px; }
  .divider {
    position: relative;
    width: 1px;
    height: 170px;
    margin-left: 20px;
    background: var(--rule);
  }
  .contact {
    position: relative;
    padding-left: 36px;
    display: flex;
    flex-direction: column;
    gap: 22px;
  }
  .contact-row { display: flex; align-items: center; gap: 18px; }
  .icon {
    width: 40px; height: 40px;
    flex: none;
  }
  .person-name {
    font-family: "Archivo", Arial, sans-serif;
    font-weight: 900;
    font-size: 24px;
    letter-spacing: 1.5px;
    color: var(--white);
    white-space: nowrap;
  }
  .person-title {
    font-family: "Archivo", Arial, sans-serif;
    font-weight: 700;
    font-size: 19px;
    letter-spacing: 1.5px;
    color: var(--blue);
  }
  .contact-text { font-size: 18px; line-height: 1.35; color: var(--text-grey); letter-spacing: 0.4px; white-space: nowrap; }
</style>
</head>
<body>
  <section class="card card-back">
    <div class="brand-name">TVK</div>
    <div class="tagline">Precision - Built Protection</div>
    <div class="back-url">WWW.BRINMORETECH.EXAMPLE</div>
  </section>

  <section class="card card-front">
    <div class="texture" role="img" aria-label="Fine dark honeycomb texture across the card"></div>
    <div class="front-logo">
      <div class="brand-name">TVK</div>
      <div class="tagline">Precision - Built Protection</div>
    </div>
    <div class="divider"></div>
    <div class="contact">
      <div class="contact-row">
        <svg class="icon" viewBox="0 0 40 40" aria-hidden="true">
          <circle cx="20" cy="20" r="18" fill="none" stroke="var(--blue)" stroke-width="2"/>
          <circle cx="20" cy="20" r="14" fill="var(--blue)"/>
          <circle cx="20" cy="16" r="4" fill="none" stroke="var(--white)" stroke-width="1.6"/>
          <path d="M12.5 28 Q20 19 27.5 28" fill="none" stroke="var(--white)" stroke-width="1.6"/>
        </svg>
        <div>
          <div class="person-name">DANIEL WHITCOMBE</div>
          <div class="person-title">CEO/FOUNDER</div>
        </div>
      </div>
      <div class="contact-row">
        <svg class="icon" viewBox="0 0 40 40" aria-hidden="true">
          <circle cx="20" cy="20" r="18" fill="none" stroke="var(--blue)" stroke-width="2"/>
          <circle cx="20" cy="20" r="14" fill="var(--blue)"/>
          <path d="M14 12.5 l3.5-1 2.5 5-2 1.6 q1.3 3.2 4.4 4.6 l1.7-2 4.9 2.5-1 3.5 q-9 1-14-14z" fill="var(--white)"/>
        </svg>
        <div class="contact-text">P: +1 555-014-2237<br>M: +1 555-014-2237</div>
      </div>
      <div class="contact-row">
        <svg class="icon" viewBox="0 0 40 40" aria-hidden="true">
          <circle cx="20" cy="20" r="18" fill="none" stroke="var(--blue)" stroke-width="2"/>
          <circle cx="20" cy="20" r="14" fill="var(--blue)"/>
          <g fill="none" stroke="var(--white)" stroke-width="1.3">
            <circle cx="20" cy="20" r="8"/>
            <ellipse cx="20" cy="20" rx="3.6" ry="8"/>
            <line x1="12" y1="20" x2="28" y2="20"/>
            <line x1="13.5" y1="15.5" x2="26.5" y2="15.5"/>
            <line x1="13.5" y1="24.5" x2="26.5" y2="24.5"/>
          </g>
        </svg>
        <div class="contact-text">daniel@brinmoretech.example<br>www.brinmoretech.example</div>
      </div>
    </div>
  </section>
</body>
</html>
```